School Website

I need a design for a School (2 sections: Primary 6-12 years and Secondary 12-18 years). The first page is just a choice of the 2 sections. After we'll need 2 websites (with the same structure: Menu, ...) but with different colors. In fact, we need for end of October, 6 design of school website. So the best websites are going to be made available to you in the future (in pixmarketo) but privately.

Target Market(s)

Public, Parents, ...

Coding

Coded - Design and coding required

Number of Pages Required

5+ page

Font styles to use
Sans Serif

Colors
34a6d7
85cae6
cee9f5
ffffff

Requirements
Must have
• You can check the old Website: http: / /velmoq.be We need the same pages with the same content. Menu: - HomePage - News and communication (like blog page) - Activities (like blog page, with photo gallery) - Contact (Contact form + maps) - In the main menu, we need a special button to connect to an external Website ( button needs to be different than the other menu items The name of this button is "Parents Area"). The logo of 2 sections are attached. Please use it for the design and the choice of colors.
Nice to have
• This is a web design of other school that we like: https://www.quintel.be

```html
<!DOCTYPE html>
<html lang="en">
<head>
<meta charset="utf-8">
<title>Athénée Royal de Velmont – Secondary School</title>
<link href="https://fonts.googleapis.com/css2?family=Fira+Sans:ital,wght@0,400;0,500;0,600;0,700;1,400&family=Open+Sans:ital,wght@0,400;0,600;0,700;1,400&display=swap" rel="stylesheet">
<style>
:root{
  --blue:#34a6d7;
  --blue-mid:#85cae6;
  --blue-light:#cee9f5;
  --white:#ffffff;
  --green:#7ab934;
  --green-dark:#5d9a22;
  --ink:#222222;
  --text:#333333;
  --muted:#777777;
  --panel:#f1f2f4;
  --footer:#3b3b3b;
  --footer-deep:#2a2a2a;
}
*{box-sizing:border-box;margin:0;padding:0}
html,body{width:1200px;height:4392px;overflow:hidden}
body{position:relative;background:var(--white);font-family:"Open Sans",sans-serif;color:var(--text)}
.abs{position:absolute}
h2.section-title{font-family:"Fira Sans",sans-serif;font-weight:600;font-size:30px;color:var(--ink);letter-spacing:.5px}
.card-shadow{background:var(--white);box-shadow:0 2px 10px rgba(0,0,0,.15)}

/* top bar */
.topbar{left:0;top:0;width:1200px;height:41px;background:var(--ink);color:var(--white);font-size:13px;font-weight:600}
.topbar .contact-item{position:absolute;top:12px;display:flex;align-items:center;gap:8px}
.topbar .social{position:absolute;top:9px;width:22px;height:22px;border:2px solid var(--white);border-radius:50%}

/* header */
.header{left:0;top:41px;width:1200px;height:92px;background:var(--white)}
.brand{position:absolute;left:51px;top:26px;display:flex;align-items:center;gap:10px}
.brand .mark{width:40px;height:40px;border-radius:50%;background:var(--blue)}
.brand .name{font-family:"Fira Sans",sans-serif;font-weight:700;font-size:22px;color:var(--blue)}
.nav{position:absolute;top:34px;font-size:14px;font-weight:600;color:var(--ink)}
.parents-btn{position:absolute;left:1006px;top:29px;width:146px;height:36px;border-radius:18px;background:var(--green);color:var(--white);font-weight:700;font-size:15px;display:flex;align-items:center;justify-content:center;box-shadow:0 3px 6px rgba(0,0,0,.3)}

/* hero */
.hero{left:0;top:133px;width:1200px;height:470px;background:linear-gradient(180deg,#2d3a2a 0%,#55624a 55%,#3c4636 100%)}
.hero .figure{position:absolute;background:linear-gradient(180deg,#d9b79a,#6f95c4);opacity:.55;border-radius:120px 120px 0 0}
.hero-text{left:0;top:240px;width:1200px;text-align:center;color:var(--white);font-family:"Fira Sans",sans-serif}
.hero-text .w1{font-size:50px;font-weight:600;line-height:60px}
.hero-text .w2{font-size:52px;font-weight:500;line-height:64px}
.hero-text .w3{font-size:25px;font-weight:500;line-height:30px}
.call-btn{left:506px;top:433px;width:188px;height:55px;border-radius:28px;background:var(--ink);color:var(--white);font-size:19px;font-weight:600;display:flex;align-items:center;justify-content:center;gap:12px}

/* info cards */
.info-card{top:685px;width:350px;height:128px;border-radius:12px;display:flex;align-items:center}
.info-card .icon{width:76px;height:76px;border-radius:50%;background:var(--ink);margin-left:28px;margin-right:34px;display:flex;align-items:center;justify-content:center;flex-shrink:0}
.info-card .label{font-size:15px;font-weight:700;color:var(--ink);line-height:22px;text-align:center}

/* schedules */
.sched-card{top:941px;width:537px;height:431px}
.sched-card .head{height:184px;border-bottom:1px solid #e3e3e3;text-align:center;padding-top:26px}
.sched-card .head h3{font-family:"Fira Sans",sans-serif;font-weight:600;font-size:19px;color:var(--green);margin-top:14px}
.sched-card ul{list-style:none;padding:22px 0 0 24px}
.sched-card li{display:flex;align-items:center;gap:30px;height:53px;font-size:13px;color:#555;text-transform:uppercase;line-height:19px}
.tick{width:28px;height:28px;border-radius:50%;background:var(--green);display:flex;align-items:center;justify-content:center;flex-shrink:0}
.note{left:0;top:1398px;width:1200px;text-align:center;font-size:13.5px;font-weight:700;color:var(--ink);line-height:23px}

/* news */
.news{left:0;top:1488px;width:1200px;height:600px;background:var(--panel)}
.arrows{display:flex;gap:18px}
.arrows span{width:28px;height:20px;background:var(--ink);display:flex;align-items:center;justify-content:center}
.news-card{top:1616px;width:348px;height:413px;border-radius:6px;overflow:hidden}
.news-card .photo{height:170px;border-bottom:4px solid var(--green);position:relative}
.date-badge{position:absolute;left:0;top:0;background:var(--ink);color:var(--white);font-family:"Fira Sans",sans-serif;font-weight:600;font-size:15px;line-height:17px;padding:6px 10px;text-align:center}
.news-card h3{font-family:"Fira Sans",sans-serif;font-weight:500;font-size:18px;color:var(--ink);margin:20px 0 0 26px}
.news-card .meta{display:flex;justify-content:space-between;font-size:13px;color:var(--muted);margin:28px 30px 0 26px}
.news-card p{font-size:12.5px;color:#888;line-height:23px;margin:18px 26px 0 26px}
.read-more{font-size:13px;font-weight:700;color:var(--green);margin:16px 0 0 26px}

/* team + contacts */
.team-wrap{left:0;top:2088px;width:1200px;height:611px;background:var(--panel)}
.team-box{left:51px;top:2140px;width:738px;height:503px}
.member{position:absolute;top:2265px;width:220px;text-align:center}
.member .avatar{width:153px;height:153px;border-radius:50%;margin:0 auto;border:8px solid var(--green);border-left-color:#e6e6e6;border-top-color:#e6e6e6;background:linear-gradient(160deg,#e6e6e6,#bfc4ca)}
.member .nm{font-family:"Fira Sans",sans-serif;font-weight:500;font-size:19px;color:#666;margin-top:18px;text-transform:uppercase}
.member .sec{font-style:italic;font-size:13px;color:#666;margin-top:6px}
.member .cls{font-size:13px;font-weight:600;color:#555;margin-top:10px}
.dot{position:absolute;top:2573px;width:14px;height:14px;border-radius:50%;background:var(--green)}
.dot.on{background:var(--white);border:3px solid var(--green);box-shadow:0 0 0 2px #cfe6b4}
.contacts-box{left:820px;top:2140px;width:332px;height:503px}
.contacts-inner{left:856px;top:2245px;width:261px;height:364px;box-shadow:0 1px 8px rgba(0,0,0,.15);background:var(--white)}
.contact-entry{margin:0 26px;padding:26px 0 16px;border-bottom:1px solid #ddd}
.contact-entry .nm{font-size:14px;font-weight:700;color:var(--ink);text-transform:uppercase}
.contact-entry .role{font-style:italic;font-size:13px;color:#888;margin-top:6px}
.contact-entry .tel{display:flex;align-items:center;gap:10px;font-size:13px;color:#555;margin-top:14px}
.btn-dark{background:var(--ink);color:var(--white);border-radius:28px;display:flex;align-items:center;justify-content:center;gap:8px;font-weight:700}

/* activities */
.activity-card{left:51px;top:2835px;width:585px;height:195px}
.activity-card .photo{position:absolute;left:0;top:0;width:234px;height:195px;background:linear-gradient(150deg,#6d7f5e,#b9c2c8 60%,#566273)}
.activity-card .date-badge{font-size:21px;line-height:28px;padding:4px 10px;text-align:left}
.act-line{position:absolute;left:258px;display:flex;align-items:center;gap:20px;font-size:13.5px;color:#555}
.rules-box{left:696px;top:2757px;width:456px;height:285px;box-shadow:0 1px 8px rgba(0,0,0,.15);background:linear-gradient(180deg,#fff 70%,#f1f8fc)}

/* gallery */
.gallery{left:0;top:3094px;width:1200px;height:538px;background:var(--panel)}
.shot{position:absolute;border:2px solid #fff;box-shadow:0 1px 6px rgba(0,0,0,.25)}

/* contact */
.map{left:51px;top:3683px;width:556px;height:426px;background:linear-gradient(135deg,#f3efe2,#e9e4cf 50%,#d7e6c4)}
.contact-panel{left:607px;top:3683px;width:544px;height:426px;background:linear-gradient(160deg,#3d4a3c,#2a3128 60%,#454d41)}
.field{position:absolute;background:var(--white);border-radius:6px;font-style:italic;font-size:13px;color:#999;padding:12px 14px}

/* footer */
.footer{left:0;top:4228px;width:1200px;height:164px;background:var(--footer)}
.footer .ring,.ring{position:absolute;top:4283px;width:42px;height:42px;border:3px solid var(--white);border-radius:50%}
.copyright{left:0;top:4344px;width:1200px;height:48px;background:var(--footer-deep);color:#bbb;font-size:13px;display:flex;align-items:center;justify-content:center}
</style>
</head>
<body>

<!-- top bar -->
<div class="abs topbar">
  <div class="contact-item" style="left:50px">
    <svg width="14" height="14" viewBox="0 0 24 24"><path fill="#fff" d="M6.6 10.8a15 15 0 0 0 6.6 6.6l2.2-2.2c.3-.3.7-.4 1-.2 1.1.4 2.3.6 3.6.6.6 0 1 .4 1 1V20c0 .6-.4 1-1 1A17 17 0 0 1 3 4c0-.6.4-1 1-1h3.5c.6 0 1 .4 1 1 0 1.3.2 2.5.6 3.6.1.3 0 .7-.2 1z"/></svg>
    +32 81 40 55 17
  </div>
  <div class="contact-item" style="left:202px">
    <svg width="16" height="14" viewBox="0 0 24 22"><path fill="#fff" d="M23 1 1 10l7 3 2 8 4-5 6 4z"/></svg>
    info@velmont-school.be
  </div>
  <span class="social" style="left:1070px"></span>
  <span class="social" style="left:1099px"></span>
  <span class="social" style="left:1128px"></span>
</div>

<!-- header -->
<header class="abs header">
  <div class="brand"><span class="mark"></span><span class="name">Athénée Royal de Velmont</span></div>
  <nav>
    <span class="nav" style="left:491px">Home</span>
    <span class="nav" style="left:570px">News</span>
    <span class="nav" style="left:642px">Activities</span>
    <span class="nav" style="left:745px">Gallery</span>
    <span class="nav" style="left:834px">Contact</span>
  </nav>
  <div class="parents-btn">Parents Area</div>
</header>

<!-- hero -->
<section class="abs hero" role="img" aria-label="Classroom photo with a smiling teacher holding an open book on the left and two smiling students carrying books on the right">
  <div class="figure" style="left:20px;top:30px;width:300px;height:440px"></div>
  <div class="figure" style="left:880px;top:20px;width:320px;height:450px"></div>
</section>
<div class="abs hero-text">
  <div class="w1">WELCOME TO</div>
  <div class="w2">Athenee Royal de Velmont</div>
  <div class="w3">Secodary School</div>
</div>
<div class="abs call-btn">
  <svg width="20" height="20" viewBox="0 0 24 24"><path fill="#fff" d="M6.6 10.8a15 15 0 0 0 6.6 6.6l2.2-2.2c.3-.3.7-.4 1-.2 1.1.4 2.3.6 3.6.6.6 0 1 .4 1 1V20c0 .6-.4 1-1 1A17 17 0 0 1 3 4c0-.6.4-1 1-1h3.5c.6 0 1 .4 1 1 0 1.3.2 2.5.6 3.6.1.3 0 .7-.2 1z"/></svg>
  Call Us
</div>
<svg class="abs" style="left:0;top:560px" width="1200" height="110" viewBox="0 0 1200 110">
  <polygon fill="#34a6d7" points="0,26 420,26 600,84 780,26 1200,26 1200,40 780,40 600,100 420,40 0,40"/>
  <polygon fill="#ffffff" points="0,40 420,40 600,100 780,40 1200,40 1200,110 0,110"/>
  <rect x="582" y="0" width="36" height="70" fill="#222"/>
  <rect x="590" y="8" width="20" height="32" rx="10" fill="none" stroke="#fff" stroke-width="2"/>
  <line x1="600" y1="16" x2="600" y2="24" stroke="#fff" stroke-width="2"/>
  <path d="M600 46v14m-5-5 5 5 5-5" stroke="#fff" stroke-width="2" fill="none"/>
</svg>

<!-- info cards -->
<div class="abs info-card card-shadow" style="left:51px">
  <div class="icon"><svg width="26" height="34" viewBox="0 0 24 32"><path fill="#fff" d="M12 0a12 12 0 0 0-12 12c0 9 12 20 12 20s12-11 12-20A12 12 0 0 0 12 0zm0 17a5 5 0 1 1 0-10 5 5 0 0 1 0 10z"/></svg></div>
  <div class="label">Rue des Tilleuls 12 / B,<br>4520 Velmont, Belgium</div>
</div>
<div class="abs info-card card-shadow" style="left:426px">
  <div class="icon"><svg width="36" height="36" viewBox="0 0 24 24"><circle cx="12" cy="12" r="10" fill="none" stroke="#fff" stroke-width="2"/><path d="M12 6v6h5" stroke="#fff" stroke-width="2" fill="none"/></svg></div>
  <div class="label" style="margin-left:32px">Monday to Friday<br>7 am - 6 pm</div>
</div>
<div class="abs info-card card-shadow" style="left:803px">
  <div class="icon"><svg width="30" height="30" viewBox="0 0 24 24"><path fill="#fff" d="M6.6 10.8a15 15 0 0 0 6.6 6.6l2.2-2.2c.3-.3.7-.4 1-.2 1.1.4 2.3.6 3.6.6.6 0 1 .4 1 1V20c0 .6-.4 1-1 1A17 17 0 0 1 3 4c0-.6.4-1 1-1h3.5c.6 0 1 .4 1 1 0 1.3.2 2.5.6 3.6.1.3 0 .7-.2 1z"/></svg></div>
  <div class="label" style="margin-left:40px">Call Us<br>+32 81 40 55 17</div>
</div>

<!-- schedules -->
<h2 class="abs section-title" style="left:0;top:856px;width:1200px;text-align:center">OUR SCHEDULES</h2>

<div class="abs sched-card card-shadow" style="left:48px">
  <div class="head">
    <svg width="92" height="92" viewBox="0 0 92 92"><circle cx="46" cy="46" r="43" fill="#1c6fb8"/><circle cx="46" cy="46" r="36" fill="#fff"/><path d="M46 18v28l16 10" stroke="#222" stroke-width="3" fill="none"/><circle cx="46" cy="46" r="3" fill="#222"/></svg>
    <h3>OUR SCHEDULES AND DAYCARE</h3>
  </div>
  <ul>
    <li><span class="tick"><svg width="14" height="14" viewBox="0 0 14 14"><path d="M2 7h9M7 3l4 4-4 4" stroke="#fff" stroke-width="2" fill="none"/></svg></span>EVERY DAY FROM 8:25 AM TO 3:25 PM</li>
    <li><span class="tick"><svg width="14" height="14" viewBox="0 0 14 14"><path d="M2 7h9M7 3l4 4-4 4" stroke="#fff" stroke-width="2" fill="none"/></svg></span>WEDNESDAYS, FROM 8:25 AM TO 12:20 PM</li>
    <li><span class="tick"><svg width="14" height="14" viewBox="0 0 14 14"><path d="M2 7h9M7 3l4 4-4 4" stroke="#fff" stroke-width="2" fill="none"/></svg></span>A DAYCARE IS ORGANIZED FROM 7:00 AM</li>
    <li><span class="tick"><svg width="14" height="14" viewBox="0 0 14 14"><path d="M2 7h9M7 3l4 4-4 4" stroke="#fff" stroke-width="2" fill="none"/></svg></span>ON WEDNESDAYS, FROM 12:30 TO 18:00,<br>&nbsp;DIFFERENT ACTIVITIES ARE OFFERED</li>
  </ul>
</div>

<div class="abs sched-card card-shadow" style="left:610px">
  <div class="head">
    <svg width="92" height="92" viewBox="0 0 92 92"><circle cx="46" cy="46" r="43" fill="#cee9f5"/><circle cx="46" cy="46" r="34" fill="#fff" stroke="#85cae6" stroke-width="4"/><circle cx="46" cy="46" r="22" fill="none" stroke="#34a6d7" stroke-width="3"/></svg>
    <h3>SCHOOL HOLIDAYS</h3>
  </div>
  <ul>
    <li><span class="tick"><svg width="14" height="14" viewBox="0 0 14 14"><path d="M2 7h9M7 3l4 4-4 4" stroke="#fff" stroke-width="2" fill="none"/></svg></span>BACK TO SCHOOL: MONDAY SEPTEMBER 3RD, 2019</li>
    <li><span class="tick"><svg width="14" height="14" viewBox="0 0 14 14"><path d="M2 7h9M7 3l4 4-4 4" stroke="#fff" stroke-width="2" fill="none"/></svg></span>FEAST OF THE FRENCH COMMUNITY: THU 27 SEPT 2019</li>
    <li><span class="tick"><svg width="14" height="14" viewBox="0 0 14 14"><path d="M2 7h9M7 3l4 4-4 4" stroke="#fff" stroke-width="2" fill="none"/></svg></span>WINTER HOLIDAYS (CHRISTMAS): DEC 24, 2019 TO JAN 4, 2020</li>
    <li><span class="tick"><svg width="14" height="14" viewBox="0 0 14 14"><path d="M2 7h9M7 3l4 4-4 4" stroke="#fff" stroke-width="2" fill="none"/></svg></span>SUMMER HOLIDAYS START ON MONDAY 1ST JULY 2020</li>
  </ul>
</div>

<div class="abs note">NOTE : ONLY THOSE CHILDREN WHOSE PARENTS HAVE PROVIDED A CERTIFICATE FROM THEIR EMPLOYER<br>SPECIFYING THE HOURS OF WORK WILL BE ACCEPTED &nbsp;AT THE DAY CARE CENTER.</div>

<!-- news -->
<section class="abs news"></section>
<h2 class="abs section-title" style="left:48px;top:1535px">NEWS</h2>
<div class="abs arrows" style="left:1074px;top:1545px">
  <span><svg width="8" height="10" viewBox="0 0 8 10"><path d="M6 1 2 5l4 4" stroke="#fff" stroke-width="1.5" fill="none"/></svg></span>
  <span><svg width="8" height="10" viewBox="0 0 8 10"><path d="M2 1l4 4-4 4" stroke="#fff" stroke-width="1.5" fill="none"/></svg></span>
</div>

<article class="abs news-card card-shadow" style="left:48px">
  <div class="photo" role="img" aria-label="Photo of smiling teenage students posing together" style="background:linear-gradient(135deg,#e6c3a2,#8db4d6 55%,#5f7d4a)"><div class="date-badge">25<br>Sept</div></div>
  <h3>Loreum Ipsum Dummy Text</h3>
  <div class="meta"><span>&#9632;&nbsp; Lucas</span><span>&#9679;&nbsp; 3 Comments</span></div>
  <p>Contrary to popular belief, Lorem Ipsum is not to simply random text. It has roots in a piece of the classi cal Latin literature.</p>
  <div class="read-more">&raquo;&nbsp; Read More</div>
</article>
<article class="abs news-card card-shadow" style="left:424px">
  <div class="photo" role="img" aria-label="Photo of students studying together with books" style="background:linear-gradient(135deg,#f0e4dc,#c99b8a 50%,#4b6b9e)"><div class="date-badge">2<br>Sept</div></div>
  <h3>Loreum Ipsum Dummy Text</h3>
  <div class="meta"><span>&#9632;&nbsp; Martin</span><span>&#9679;&nbsp; 3 Comments</span></div>
  <p>Contrary to popular belief, Lorem Ipsum is not to simply random text. It has roots in a piece of the classi cal Latin literature.</p>
  <div class="read-more">&raquo;&nbsp; Read More</div>
</article>
<article class="abs news-card card-shadow" style="left:800px">
  <div class="photo" role="img" aria-label="Photo of a group of smiling students in a school hallway" style="background:linear-gradient(135deg,#6a5a5a,#c9a58a 50%,#7a8fa8)"><div class="date-badge">20<br>Sept</div></div>
  <h3>Loreum Ipsum Dummy Text</h3>
  <div class="meta"><span>&#9632;&nbsp; Thomas</span><span>&#9679;&nbsp; 3 Comments</span></div>
  <p>Contrary to popular belief, Lorem Ipsum is not to simply random text. It has roots in a piece of the classi cal Latin literature.</p>
  <div class="read-more">&raquo;&nbsp; Read More</div>
</article>

<!-- team -->
<section class="abs team-wrap"></section>
<div class="abs team-box card-shadow"></div>
<h2 class="abs section-title" style="left:51px;top:2183px;width:738px;text-align:center">OUR TEACHING TEAM</h2>
<div class="member" style="left:57px"><div class="avatar" role="img" aria-label="Portrait photo of teacher Laure Mertens"></div><div class="nm">Laure Mertens</div><div class="sec">Kindergarten section</div><div class="cls">Holder of the class of M1</div></div>
<div class="member" style="left:311px"><div class="avatar" role="img" aria-label="Portrait photo of teacher Claire Dufour"></div><div class="nm">Claire Dufour</div><div class="sec">Primary section</div><div class="cls">Holder of P1 class</div></div>
<div class="member" style="left:572px"><div class="avatar" role="img" aria-label="Portrait photo of teacher Mr Julien"></div><div class="nm">Mr Julien</div><div class="sec">Primary section</div><div class="cls">Holder of P6 class</div></div>
<span class="dot on" style="left:360px;top:2571px;width:18px;height:18px"></span>
<span class="dot" style="left:397px"></span>
<span class="dot" style="left:431px"></span>
<span class="dot" style="left:465px"></span>

<div class="abs contacts-box card-shadow"></div>
<h2 class="abs section-title" style="left:820px;top:2184px;width:332px;text-align:center">USEFUL CONTACTS</h2>
<div class="abs contacts-inner">
  <div class="contact-entry">
    <div class="nm">Mrs Hélène Maréchal</div>
    <div class="role">Prefect of studies</div>
    <div class="tel"><svg width="16" height="16" viewBox="0 0 24 24"><path fill="#34a6d7" d="M6.6 10.8a15 15 0 0 0 6.6 6.6l2.2-2.2c.3-.3.7-.4 1-.2 1.1.4 2.3.6 3.6.6.6 0 1 .4 1 1V20c0 .6-.4 1-1 1A17 17 0 0 1 3 4c0-.6.4-1 1-1h3.5c.6 0 1 .4 1 1 0 1.3.2 2.5.6 3.6.1.3 0 .7-.2 1z"/></svg>081 -40-5518</div>
  </div>
  <div class="contact-entry">
    <div class="nm">Mrs Sophie Dorval</div>
    <div class="role">Secretariat</div>
    <div class="tel"><svg width="16" height="16" viewBox="0 0 24 24"><path fill="#34a6d7" d="M6.6 10.8a15 15 0 0 0 6.6 6.6l2.2-2.2c.3-.3.7-.4 1-.2 1.1.4 2.3.6 3.6.6.6 0 1 .4 1 1V20c0 .6-.4 1-1 1A17 17 0 0 1 3 4c0-.6.4-1 1-1h3.5c.6 0 1 .4 1 1 0 1.3.2 2.5.6 3.6.1.3 0 .7-.2 1z"/></svg>081 -40-5518</div>
  </div>
</div>
<div class="abs btn-dark" style="left:907px;top:2530px;width:159px;height:45px;font-size:14px">View All <svg width="16" height="12" viewBox="0 0 16 12"><path d="M1 6h13M9 1l5 5-5 5" stroke="#fff" stroke-width="2" fill="none"/></svg></div>

<!-- activities -->
<h2 class="abs section-title" style="left:55px;top:2750px">ACTIVITIES</h2>
<div class="abs arrows" style="left:562px;top:2787px">
  <span><svg width="8" height="10" viewBox="0 0 8 10"><path d="M6 1 2 5l4 4" stroke="#fff" stroke-width="1.5" fill="none"/></svg></span>
  <span><svg width="8" height="10" viewBox="0 0 8 10"><path d="M2 1l4 4-4 4" stroke="#fff" stroke-width="1.5" fill="none"/></svg></span>
</div>
<div class="abs activity-card card-shadow">
  <div class="photo" role="img" aria-label="Photo of children in beekeeping suits during an outdoor activity"><div class="date-badge">SEPT<br>&nbsp;20</div></div>
  <div class="abs" style="left:261px;top:36px;font-family:'Fira Sans',sans-serif;font-weight:500;font-size:19px;color:var(--ink)">Loreum ipsum dummy text</div>
  <div class="act-line" style="top:80px"><svg width="22" height="22" viewBox="0 0 24 24"><circle cx="12" cy="12" r="10" fill="none" stroke="#7ab934" stroke-width="2"/><path d="M12 7v5h4" stroke="#7ab934" stroke-width="2" fill="none"/></svg>12:00 p.m - 5:00 p.m</div>
  <div class="act-line" style="top:126px"><svg width="20" height="24" viewBox="0 0 24 32"><path fill="#7ab934" d="M12 0a12 12 0 0 0-12 12c0 9 12 20 12 20s12-11 12-20A12 12 0 0 0 12 0zm0 17a5 5 0 1 1 0-10 5 5 0 0 1 0 10z"/></svg>Loreum ipsum dummy text ,14th Etd.</div>
</div>
<div class="abs" style="left:662px;top:2748px;width:1px;height:287px;background:#ddd"></div>
<div class="abs rules-box">
  <h2 class="section-title" style="text-align:center;margin-top:32px">RULES OF PROCEDURE</h2>
  <div style="text-align:center;font-size:18px;color:#777;line-height:28px;margin-top:12px">Please find attached the rules<br>of procedure:</div>
</div>
<div class="abs btn-dark" style="left:820px;top:2922px;width:208px;height:72px;font-size:14px;line-height:18px;gap:14px">
  <svg width="24" height="24" viewBox="0 0 24 24"><rect x="3" y="3" width="14" height="18" rx="1" fill="none" stroke="#fff" stroke-width="2"/><path d="M7 9h6M7 13h6M14 20l7-7" stroke="#fff" stroke-width="2"/></svg>
  <span style="text-align:center">Click Here to find<br>Attachmet</span>
</div>

<!-- gallery -->
<section class="abs gallery"></section>
<h2 class="abs section-title" style="left:48px;top:3138px">GALLERY</h2>
<div class="abs arrows" style="left:1077px;top:3149px">
  <span><svg width="8" height="10" viewBox="0 0 8 10"><path d="M6 1 2 5l4 4" stroke="#fff" stroke-width="1.5" fill="none"/></svg></span>
  <span><svg width="8" height="10" viewBox="0 0 8 10"><path d="M2 1l4 4-4 4" stroke="#fff" stroke-width="1.5" fill="none"/></svg></span>
</div>
<div class="shot" role="img" aria-label="Photo of smiling students giving thumbs up in a classroom" style="left:48px;top:3219px;width:344px;height:358px;background:linear-gradient(150deg,#4d5a3c,#d7b08f 50%,#8f6fa8)"></div>
<div class="shot" role="img" aria-label="Photo of a teacher speaking to a class of students" style="left:430px;top:3219px;width:334px;height:171px;background:linear-gradient(160deg,#e9e4dc,#b9a38e 55%,#6b4a3a)"></div>
<div class="shot" role="img" aria-label="Photo of uniformed students standing by stacks of books on a yellow background" style="left:430px;top:3407px;width:334px;height:170px;background:linear-gradient(180deg,#f3c233,#e6a71f 60%,#3f5f9a)"></div>
<div class="shot" role="img" aria-label="Photo of a thoughtful student holding notebooks in front of a chalkboard" style="left:801px;top:3219px;width:347px;height:358px;background:linear-gradient(150deg,#3a3d3c,#6b6e6c 45%,#c89a72)"></div>

<!-- contact -->
<div class="abs map" role="img" aria-label="Road map of Belgium, the Netherlands and western Germany with a red pin on the school location"></div>
<div class="abs contact-panel" role="img" aria-label="Photo of the school building behind trees, darkened"></div>
<h2 class="abs section-title" style="left:607px;top:3736px;width:544px;text-align:center;color:#fff">CONTACT US</h2>
<div class="field" style="left:660px;top:3819px;width:198px;height:41px">Name</div>
<div class="field" style="left:898px;top:3819px;width:198px;height:41px">Email</div>
<div class="field" style="left:660px;top:3892px;width:433px;height:75px">Message</div>
<div class="abs btn-dark" style="left:801px;top:4006px;width:154px;height:52px;font-size:19px">
  <svg width="18" height="18" viewBox="0 0 24 22"><path fill="#fff" d="M23 1 1 10l7 3 2 8 4-5 6 4z"/></svg>Submit
</div>

<!-- footer -->
<svg class="abs" style="left:0;top:4140px" width="1200" height="90" viewBox="0 0 1200 90">
  <polygon fill="#3b3b3b" points="0,84 460,84 530,48 670,48 740,84 1200,84 1200,90 0,90"/>
  <polyline fill="none" stroke="#34a6d7" stroke-width="5" points="0,84 460,84 530,48 670,48 740,84 1200,84"/>
  <path d="M600 4v14m-5-9 5-5 5 5" stroke="#222" stroke-width="2" fill="none"/>
  <rect x="591" y="24" width="18" height="30" rx="9" fill="none" stroke="#222" stroke-width="2"/>
</svg>
<footer class="abs footer"></footer>
<span class="ring" style="left:494px"></span>
<span class="ring" style="left:552px"></span>
<span class="ring" style="left:610px"></span>
<span class="ring" style="left:664px"></span>
<div class="abs copyright">© 2019 Copyrights &nbsp;@ Athénée Royal de Velmont All Rights Reserved</div>

</body>
</html>
```